Business Card Design for Varnel

I've already got the logo, but I'd like to see some interesting designs.

I don't want anything to complex. I like it simple,yet innovative, like the logo.

My business is System Administration for small to medium size businesses, so that will be my main target audience.
Updates

hey all, the png has been uploaded.

Hey all,

If you are submitting the back side of the card, I'd like the top bit of the card to be Varnel Solutions and the logo, the bottom of the card the website, with a white background.

The middle I'd like to leave blank for a quote that will be printed on each card.

Thanks!

Doug

Industry/Entity Type

Business

```html
<!DOCTYPE html>
<html lang="en">
<head>
<meta charset="utf-8">
<title>Varnel Solutions – Business Card</title>
<link rel="stylesheet" href="https://fonts.googleapis.com/css2?family=Arimo:wght@400;700&family=Archivo+Narrow:wght@600&display=swap">
<style>
  :root {
    --card-light: #ffffff;
    --card-shade: #e9e9ea;
    --brand-blue: #2f80c0;
    --rule-blue: #1a6aa3;
    --rule-grey: #4d4a48;
    --ink-dark: #231f20;
    --ink-grey: #55565a;
  }
  html, body {
    margin: 0;
    padding: 0;
    overflow: hidden;
    background: var(--card-light);
  }
  .card {
    position: relative;
    width: 1200px;
    height: 709px;
    overflow: hidden;
    background: radial-gradient(ellipse at 85% 10%, var(--card-light) 0%, #f6f6f6 45%, var(--card-shade) 100%);
    font-family: "Arimo", Arial, sans-serif;
  }
  .brand {
    position: absolute;
    left: 700px;
    top: 32px;
    display: flex;
    align-items: center;
    gap: 36px;
  }
  .brand-mark {
    width: 150px;
    height: 150px;
    border-radius: 50%;
    background: var(--brand-blue);
  }
  .brand-name {
    color: var(--brand-blue);
    font-weight: 400;
    line-height: 1;
  }
  .brand-name .word {
    display: block;
    font-size: 84px;
    letter-spacing: -1px;
  }
  .brand-name .sub {
    display: block;
    font-size: 22px;
    letter-spacing: 0.62em;
    margin-top: 8px;
  }
  .company-message {
    position: absolute;
    left: 0;
    width: 1200px;
    top: 202px;
    text-align: center;
    margin: 0;
    font-size: 47px;
    font-weight: 700;
    color: var(--ink-dark);
    line-height: 1;
  }
  .person {
    position: absolute;
    left: 69px;
    top: 311px;
    color: var(--ink-grey);
    line-height: 1;
  }
  .person-name {
    font-size: 36px;
    font-weight: 700;
    margin: 0;
  }
  .person-role {
    font-size: 27px;
    margin: 5px 0 0;
  }
  .contact {
    position: absolute;
    left: 69px;
    top: 396px;
    margin: 0;
  }
  .contact-row {
    display: flex;
    align-items: baseline;
    height: 50px;
  }
  .contact-row.address { height: auto; }
  .contact-label {
    width: 150px;
    font-size: 37px;
    font-weight: 700;
    font-variant: small-caps;
    color: var(--ink-grey);
    line-height: 1;
  }
  .contact-colon {
    width: 33px;
    font-size: 30px;
    font-weight: 700;
    color: var(--ink-grey);
  }
  .contact-value {
    margin: 0;
    font-family: "Archivo Narrow", "Arial Narrow", sans-serif;
    font-weight: 600;
    font-size: 28px;
    color: var(--ink-dark);
    line-height: 1.27;
  }
  .rule {
    position: absolute;
    top: 649px;
    height: 9px;
  }
  .rule-grey { left: 0; width: 245px; background: var(--rule-grey); }
  .rule-blue { left: 300px; right: 0; background: var(--rule-blue); }
</style>
</head>
<body>
  <div class="card">
    <div class="brand">
      <div class="brand-mark"></div>
      <div class="brand-name"><span class="word">Varnel</span><span class="sub">solutions</span></div>
    </div>

    <h1 class="company-message">Company Message</h1>

    <div class="person">
      <p class="person-name">Name</p>
      <p class="person-role">Designation</p>
    </div>

    <dl class="contact">
      <div class="contact-row">
        <dt class="contact-label">Phone</dt><span class="contact-colon">:</span>
        <dd class="contact-value">Enter phone number here</dd>
      </div>
      <div class="contact-row">
        <dt class="contact-label">Email</dt><span class="contact-colon">:</span>
        <dd class="contact-value">Enter mail ID here</dd>
      </div>
      <div class="contact-row">
        <dt class="contact-label">Website</dt><span class="contact-colon">:</span>
        <dd class="contact-value">Enter web address here</dd>
      </div>
      <div class="contact-row address">
        <dt class="contact-label">Address</dt><span class="contact-colon">:</span>
        <dd class="contact-value">Address line 1<br>Address line 2</dd>
      </div>
    </dl>

    <div class="rule rule-grey"></div>
    <div class="rule rule-blue"></div>
  </div>
</body>
</html>
```